Stationary for Owner's Rep / Developer / Project Manager
Tallbrook Advisors - Gather • Shape • Deliver
Creative Brief
Professional
Desmond Farrell, AIA
Manager
27408 W. Kessler Brook Pkwy
Tampa, FL 33792
d.farrell@tallbrookadv-mail.com
www.tallbrookadv-mail.com
Company name is Tallbrook Advisors. Corporate brand is "Gather • Shape • Deliver". Would be nice if the brand could be incorporated into the design.
Card should reflect the industries that I serve - developers, architects, contractors and banks. I lead the team, organizing schedules, money, etc. Card could be a unique shape but doesn't have to, just needs to be unique and convey leadership.
Back is up to the designer. Maybe name is only on the front, details on the back? Maybe just the logo?
While I like a lot of them (all of the 3 stars +), I still haven't seen anything that blows the others away. Just looking for some unique edge - I could see a lot of the current ones, with a few modifications getting to that level. Would love to see the push of creativity, of uniqueness, of professionalism. They have to trust me with millions of dollars, the card has to show that they can.
I don't like when the entire logo, full color, etc is on one side of the card. Watermarking, or showing is a portion is OK, but the card is so small to see the entire "eye" logo twice is too much.
Draft #127, #124, #122 I like the colors, just not the configuration (I do like the "watermark" in #127. Maybe a 2.5" x 2.5" format?
For everyone - thanks for the multitude of submittals - I have a 2.5x2.5 card in my business now, people either love it or hate it, but EVERYBODY comments on it. That's what I want. Not that it has to be 2.5x2.5", but I am looking for something unique to the card.
I forgot to put the #150 on my address - the address on the card should read
27408 W. Kessler Brook Pkwy #150 - Sorry!
Would like my name to be large, easy to see on the business card, similar to Draft #1 or Draft #14.
Letterhead does not need my name (Desmond Farrell).
Look forward to seeing all of the great designers' work. I am equally interested in stationary/letterhead as the business card. Often times, the two will be presented together (a proposal/schedule with a business card attached to it). Hope to see at least both (if not more types) in the proposals.

```html
<!DOCTYPE html>
<html lang="en">
<head>
<meta charset="utf-8">
<title>Tallbrook Advisors – Stationery Concepts</title>
<link href="https://fonts.googleapis.com/css2?family=Cinzel:wght@600&family=Marcellus&family=Tinos&display=swap" rel="stylesheet">
<style>
:root{
  --bg-dark:#5e5e5e;
  --bg-light:#8c8c8c;
  --navy:#14306e;
  --blue:#1f5fae;
  --sky:#3f8fd0;
  --green:#5c9e24;
  --lime:#8cc43c;
  --green-dark:#2f6a18;
  --paper:#ffffff;
  --paper-shade:#f1f2f3;
  --ink:#2a2a2a;
  --label:#f2f2f2;
}
*{margin:0;padding:0;box-sizing:border-box}
html,body{width:1200px;height:410px;overflow:hidden}
body{
  position:relative;
  background:radial-gradient(ellipse at 50% 30%,var(--bg-light),var(--bg-dark));
  font-family:"Tinos",serif;color:var(--ink);
}
.abs{position:absolute}
.wordmark{font-family:"Cinzel",serif;font-weight:600;color:var(--blue);line-height:1.05;letter-spacing:.04em}
.tagline{font-family:"Marcellus",serif;letter-spacing:.2em;color:#fff;white-space:nowrap}
.label{font-family:"Tinos",serif;font-size:6.5px;color:var(--label);white-space:nowrap}

/* brand block */
.brand{left:30px;top:78px;width:220px;text-align:center}
.brand .dot{display:inline-block;width:14px;height:14px;border-radius:50%;background:var(--green);vertical-align:middle;margin-right:6px}
.brand .wordmark{display:inline-block;vertical-align:middle;font-size:20px;text-align:left}
.brand-title{left:124px;top:129px;font-family:"Marcellus",serif;font-size:10px;color:#fff}

/* business cards */
.card{position:absolute;width:112px;height:112px;overflow:hidden;box-shadow:0 1px 3px rgba(0,0,0,.45)}
.card-blue{left:30px;top:158px;background:radial-gradient(circle at 50% 35%,var(--sky),var(--navy))}
.card-white{left:149px;top:158px;background:var(--paper)}
.card-green-back{left:29px;top:283px;background:radial-gradient(circle at 55% 40%,var(--lime),var(--green-dark))}
.card-green-front{left:149px;top:282px;background:radial-gradient(circle at 50% 35%,var(--lime),var(--green-dark))}
.card .wordmark{position:absolute;left:0;right:0;text-align:center;color:#fff;font-size:10px}
.card .tagline{position:absolute;left:0;right:0;text-align:center;font-size:5.5px}
.card-white .wordmark{color:var(--blue);font-size:9.5px;top:14px}
.person{position:absolute;left:0;right:0;top:47px;text-align:center}
.person .name{font-family:"Cinzel",serif;font-weight:600;font-size:5.6px;color:var(--navy);letter-spacing:.03em}
.person .role{font-family:"Cinzel",serif;font-weight:600;font-size:4px;color:var(--green);margin-top:2px}
.details{position:absolute;left:0;right:0;top:69px;text-align:center;font-size:4.2px;line-height:1.3}
.details .gap{height:4px}
.details svg{width:4px;height:4px;vertical-align:-0.5px;margin-right:1px}
.band{position:absolute;left:0;right:0;bottom:0;height:7px;background:linear-gradient(90deg,var(--navy),var(--blue) 60%,var(--lime))}
.band span{position:absolute;top:1px;font-size:3.8px;letter-spacing:.15em;color:#fff;font-family:"Marcellus",serif}

/* letterheads */
.sheet{position:absolute;top:19px;width:262px;height:371px;background:linear-gradient(180deg,var(--paper),var(--paper-shade));box-shadow:0 1px 4px rgba(0,0,0,.4)}
.sheet-one{left:281px}
.sheet-two{left:558px}
.sheet .band{height:6px}
.sheet .band span{left:62px;font-size:3.6px;top:1px}
.sheet-one .wordmark{position:absolute;left:12px;top:12px;font-size:9.5px}
.sheet-one .address{position:absolute;left:188px;top:8px;padding-left:4px;border-left:.5px solid #999;font-size:4px;line-height:1.45}
.sheet-two .wordmark{position:absolute;left:0;right:0;top:12px;text-align:center;font-size:9.5px}
.sheet-two .footer-line{position:absolute;left:6px;bottom:8px;font-size:3.9px;white-space:nowrap}
.sheet-two .footer-line b{font-weight:700}
.lbl-one{left:380px;top:394px}
.lbl-two{left:655px;top:394px}

/* envelopes */
.envelope{position:absolute;width:287px;height:124px;background:var(--paper);box-shadow:0 1px 4px rgba(0,0,0,.4);overflow:hidden}
.envelope svg.flap{position:absolute;left:0;top:0;width:287px;height:124px}
.envelope .web{position:absolute;left:0;right:0;text-align:center;font-family:"Marcellus",serif;font-size:3.8px;letter-spacing:.12em}
.envelope .mark{position:absolute;left:0;right:0;text-align:center}
.envelope .mark i{display:inline-block;width:12px;height:12px;border-radius:50%}
.env-blue{left:858px;top:51px}
.env-green{left:891px;top:119px}
.env-white{left:852px;top:191px}
.env-front{left:836px;top:264px}
.env-front .wordmark{position:absolute;left:7px;top:12px;font-size:9px}
.env-front .return{position:absolute;left:6px;top:35px;font-size:4px;white-space:nowrap}
.env-front .band{height:5px}
.lbl-env{left:943px;top:394px}
</style>
</head>
<body>

<section class="abs brand">
  <span class="dot"></span><span class="wordmark">Tallbrook<br>Advisors</span>
</section>
<div class="abs brand-title">Stationary Concepts</div>

<!-- business cards -->
<div class="card card-blue">
  <div class="wordmark" style="top:64px">Tallbrook<br>Advisors</div>
  <div class="tagline" style="top:95px">Gather • Shape • Deliver</div>
</div>

<div class="card card-white">
  <div class="wordmark">Tallbrook Advisors</div>
  <div class="person">
    <div class="name">DESMOND FARRELL, AIA</div>
    <div class="role">MANAGER</div>
  </div>
  <div class="details">
    27408 W. Kessler Brook<br>Pkwy #150, Tampa, FL 33792
    <div class="gap"></div>
    <svg viewBox="0 0 10 10"><path d="M2 1l2 0 1 2-1.5 1a6 6 0 0 0 2.5 2.5L7 5l2 1v2l-1 1C4 9 1 6 1 2z" fill="#1f5fae"/></svg>813.555.0142<br>
    <svg viewBox="0 0 10 10"><rect x="1" y="2.5" width="8" height="5.5" fill="#1f5fae"/><path d="M1 2.5l4 3 4-3" stroke="#fff" stroke-width=".8" fill="none"/></svg>d.farrell@tallbrookadv-mail.com
  </div>
  <div class="band"><span style="left:13px">www.tallbrookadv-mail.com</span></div>
</div>

<div class="card card-green-back">
  <div class="tagline" style="top:56px">Gather • Shape • Deliver</div>
  <div class="tagline" style="top:65px;font-size:4.3px">www.tallbrookadv-mail.com</div>
</div>

<div class="card card-green-front">
  <div class="wordmark" style="top:62px">Tallbrook<br>Advisors</div>
  <div class="tagline" style="top:94px">Gather • Shape • Deliver</div>
</div>

<!-- letterheads -->
<article class="sheet sheet-one">
  <div class="wordmark">Tallbrook<br>Advisors</div>
  <div class="address">
    27408 W. Kessler Brook<br>Pkwy #150, Tampa, FL 33792<br>
    813.555.0142<br>d.farrell@tallbrookadv-mail.com
  </div>
  <div class="band"><span>www.tallbrookadv-mail.com</span></div>
</article>
<div class="abs label lbl-one">Letterhead option_01</div>

<article class="sheet sheet-two">
  <div class="wordmark">Tallbrook<br>Advisors</div>
  <div class="footer-line">27408 W. Kessler Brook Pkwy #150, Tampa, FL 33792 <b>P:</b> 813.555.0142 <b>E:</b> d.farrell@tallbrookadv-mail.com</div>
  <div class="band"><span>www.tallbrookadv-mail.com</span></div>
</article>
<div class="abs label lbl-two">Letterhead option_02</div>

<!-- envelopes -->
<div class="envelope env-blue">
  <svg class="flap" viewBox="0 0 287 124"><defs><linearGradient id="gBlue" x1="0" x2="0" y1="0" y2="1"><stop offset="0" stop-color="#14306e"/><stop offset="1" stop-color="#3f8fd0"/></linearGradient></defs>
    <path d="M40 124L130 70M250 124L170 70" stroke="#ddd" stroke-width=".6"/>
    <path d="M0 0H287V16Q230 40 160 52Q143 56 126 52Q60 40 0 16Z" fill="url(#gBlue)"/></svg>
  <div class="mark" style="top:10px"><i style="background:#fff"></i></div>
  <div class="web" style="top:33px;color:#fff">www.tallbrookadv-mail.com</div>
</div>

<div class="envelope env-green">
  <svg class="flap" viewBox="0 0 287 124"><defs><linearGradient id="gGreen" x1="0" x2="0" y1="0" y2="1"><stop offset="0" stop-color="#2f6a18"/><stop offset="1" stop-color="#8cc43c"/></linearGradient></defs>
    <path d="M40 124L130 70M250 124L170 70" stroke="#ddd" stroke-width=".6"/>
    <path d="M0 0H287V16Q230 40 160 52Q143 56 126 52Q60 40 0 16Z" fill="url(#gGreen)"/></svg>
  <div class="mark" style="top:10px"><i style="background:#fff"></i></div>
  <div class="web" style="top:33px;color:#fff">www.tallbrookadv-mail.com</div>
</div>

<div class="envelope env-white">
  <svg class="flap" viewBox="0 0 287 124">
    <path d="M40 124L130 70M250 124L170 70" stroke="#ddd" stroke-width=".6"/>
    <path d="M0 0H287V16Q230 40 160 52Q143 56 126 52Q60 40 0 16Z" fill="#fafafa" stroke="#ccc" stroke-width=".6"/></svg>
  <div class="mark" style="top:10px"><i style="background:var(--blue)"></i></div>
  <div class="web" style="top:34px;color:#222">www.tallbrookadv-mail.com</div>
</div>

<div class="envelope env-front">
  <div class="wordmark">Tallbrook<br>Advisors</div>
  <div class="return">27408 W. Kessler Brook Pkwy #150, Tampa, FL 33792</div>
  <div class="band"></div>
</div>
<div class="abs label lbl-env">Envelope Front &amp; Back</div>

</body>
</html>
```